Restaurant menu design

I need a menu for a restaurant in Spain.
It has to be bohemian but modern. We need something romantic and elegant.
The restaurant is elegant with good food and an excellent reputation. It is also modern at the same time.
The restaurant is superbly decorated and very chick so we need something "class" to fit in with the surroundings.
The size of the document must be 325 mm in high and 245 mm as a maximum and preferably made in indesign.

Reason: Thank you all for your designs.
So far all your designs are ok but it isn´t what we are looking for. Most of the designs are too loaded, too many colors and too much decoration.

Target Market(s)

Adults of various age groups and different nationalities mostly European.

Industry/Entity Type

Restaurant

Requirements
Must have
• The menu must have two interior pages with the text as in the document attached.It must be easily legible.
Nice to have
• See what kind of menus they use in important restaurants in places like Paris, see what designs are in trend, but Not necessarily doing the same style if it doesn’t fit in with the description above.
Should not have
• Nothing old fashioned.

```html
<!DOCTYPE html>
<html lang="es">
<head>
<meta charset="utf-8">
<title>La Volière — Carta</title>
<link href="https://fonts.googleapis.com/css2?family=Parisienne&family=Josefin+Sans:ital,wght@1,300&family=Open+Sans:wght@700&display=swap" rel="stylesheet">
<style>
  :root {
    --paper: #ffffff;
    --accent: #b3164f;
    --ink: #3a3a3a;
    --price: #8c8c8c;
  }
  * { margin: 0; padding: 0; box-sizing: border-box; }
  html, body { width: 1200px; height: 794px; overflow: hidden; background: var(--paper); }
  .spread { position: relative; width: 1200px; height: 794px; background: var(--paper); }

  .heading {
    position: absolute;
    font-family: "Parisienne", cursive;
    font-weight: 400;
    color: var(--accent);
    font-size: 27px;
    line-height: 1;
    transform: translate(-50%, -50%);
    white-space: nowrap;
  }

  .menu-list { position: absolute; list-style: none; }
  .menu-list--left { left: 145px; width: 312px; }
  .menu-list--right { left: 731px; width: 341px; }

  .item {
    display: flex;
    justify-content: space-between;
    align-items: center;
    gap: 12px;
    height: 22.3px;
    font-family: "Josefin Sans", sans-serif;
    font-style: italic;
    font-weight: 300;
    font-size: 11.4px;
    letter-spacing: -0.2px;
    color: var(--ink);
    white-space: nowrap;
  }
  .item > span:first-child { flex: 1 1 auto; min-width: 0; }
  .item--compact { height: 18.9px; }
  .item--kids { height: 20px; font-size: 10.8px; }
  .item--note { height: 35px; align-items: flex-start; padding-top: 4px; }
  .item--double { height: 38px; align-items: flex-end; padding-bottom: 4px; }

  .item__name { display: flex; flex-direction: column; line-height: 1.3; }
  .item__desc { font-size: 7px; line-height: 1.4; letter-spacing: 0; }

  .price {
    flex: 0 0 auto;
    font-family: "Open Sans", sans-serif;
    font-style: normal;
    font-weight: 700;
    font-size: 11px;
    letter-spacing: 0;
    color: var(--price);
  }

  .sauces {
    position: absolute;
    left: 900px;
    transform: translateX(-50%);
    font-family: "Josefin Sans", sans-serif;
    font-style: italic;
    font-weight: 300;
    font-size: 11px;
    color: var(--ink);
    white-space: nowrap;
    text-align: center;
  }
  .sauces__title {
    font-family: "Parisienne", cursive;
    font-style: normal;
    font-size: 30px;
    color: var(--accent);
    vertical-align: -4px;
    margin-right: 6px;
  }
  .sauces .price { margin: 0 6px 0 10px; }
  .sauces .sep { color: var(--price); margin: 0 4px; }
</style>
</head>
<body>
<main class="spread">

  <h2 class="heading" style="left:301px; top:62px;">Entradas</h2>
  <ul class="menu-list menu-list--left" style="top:83px;">
    <li class="item"><span>Ensalada La Volière. Lechuga, tomate</span><span class="price">7,75 €</span></li>
    <li class="item"><span>Ensalada Caprese (Tomate y Mozzarella)</span><span class="price">7,75 €</span></li>
    <li class="item"><span>Escarola al Queso de Cabra con Bacon</span><span class="price">6,75 €</span></li>
    <li class="item"><span>Cocktail de Gambas, Langostinos y Aguacate</span><span class="price">7,50 €</span></li>
    <li class="item"><span>La Sopa de Pescado</span><span class="price">8,25 €</span></li>
    <li class="item"><span>Crema de Espárragos Trigueros y Calabacín</span><span class="price">5,95 €</span></li>
    <li class="item"><span>Carpaccio de Ternera</span><span class="price">11,50 €</span></li>
    <li class="item"><span>Carpaccio de Salmón al Eneldo</span><span class="price">9,75 €</span></li>
    <li class="item"><span>Carpaccio de Atún</span><span class="price">13,95 €</span></li>
    <li class="item"><span>Melón con Jamón Ibérico</span><span class="price">9,25 €</span></li>
    <li class="item"><span>Parrillada de Verduras</span><span class="price">7,95 €</span></li>
    <li class="item"><span>Parrillada de Verduras Gratinada al Queso de Cabra</span><span class="price">8,95 €</span></li>
    <li class="item"><span>Gambas Roja de la Bahía</span><span class="price">12,95 €</span></li>
  </ul>

  <h2 class="heading" style="left:301px; top:424px;">Pescados al Grill</h2>
  <ul class="menu-list menu-list--left" style="top:447px;">
    <li class="item"><span>Lubina al Hinojo</span><span class="price">15,50 €</span></li>
    <li class="item"><span>Lubina Fileteada y su Salsa Rústica con Berenjena</span><span class="price">18,50 €</span></li>
    <li class="item"><span>Filete de Rodaballo y su Salsa de Marisco</span><span class="price">17,25 €</span></li>
    <li class="item"><span>Dorada del Mediterráneo</span><span class="price">13,95 €</span></li>
    <li class="item"><span>Lenguado al Grill con Hierbas Provenzales</span><span class="price">20,75 €</span></li>
    <li class="item"><span>Pieza de Atún Fresco y su Salsa Griega</span><span class="price">18,95 €</span></li>
    <li class="item"><span>Lomo de Salmón con Salsa de Frambuesa</span><span class="price">11,25 €</span></li>
    <li class="item"><span>Parrillada de Pescado y Marisco</span><span class="price">23,505 €</span></li>
  </ul>

  <h2 class="heading" style="left:301px; top:686px;">Especial Niños</h2>
  <ul class="menu-list menu-list--left" style="top:712px;">
    <li class="item item--kids"><span>Solomillo Junior, huevo y patatas fritas</span><span class="price">6,25 €</span></li>
    <li class="item item--kids"><span>Fish &amp; chips</span><span class="price">6,25 €</span></li>
  </ul>

  <h2 class="heading" style="left:903px; top:62px;">Carnes</h2>
  <ul class="menu-list menu-list--right" style="top:81px;">
    <li class="item"><span>Pechuga de Pollo “Marie Louise” con Champiñones y Bacon</span><span class="price">11,95 €</span></li>
    <li class="item"><span>Chuletas de Cordero</span><span class="price">14,50 €</span></li>
    <li class="item"><span>Costillas de Cerdo con Salsa Barbacoa</span><span class="price">9,95 €</span></li>
    <li class="item"><span>Paletilla de Cordero Lechal</span><span class="price">19,75 €</span></li>
    <li class="item item--note"><span class="item__name">Le Strogonoff.<span class="item__desc">Finas tiras de Solomillo con su Salsa de Champiñones</span></span><span class="price">15,90 €</span></li>
    <li class="item"><span>Solomillo de Ternera</span><span class="price">18,50 €</span></li>
    <li class="item item--double"><span class="item__name">Solomillo de Ternera a la Ibérica con<span>Jamón Ibérico y Ligera Salsa de Vino Tinto</span></span><span class="price">20,75 €</span></li>
    <li class="item item--note"><span class="item__name">“Hamburger Maison Steak Haché”.<span class="item__desc">Picata de Solomillo de Ternera, Huevo Frito y Patatas Fritas</span></span><span class="price">14,50 €</span></li>
    <li class="item"><span>Solomillo de Cerdo al Horno con Bacon y su Salsa de Setas</span><span class="price">14,25 €</span></li>
    <li class="item"><span>Entrecôte de Ternera</span><span class="price">14,75 €</span></li>
    <li class="item"><span>T-Bone Steak de Ternera</span><span class="price">16,75 €</span></li>
    <li class="item"><span>Chuletón de Ternera</span><span class="price">20,25 €</span></li>
    <li class="item"><span>Parrillada de Carnes y Embutidos</span><span class="price">21,50 €</span></li>
  </ul>

  <p class="sauces" style="top:436px;"><span class="sauces__title">Salsa;</span>Pimienta.<span class="price">2,85 €</span><span class="sep">·</span>Roquefort.<span class="price">2,95 €</span></p>
  <p class="sauces" style="top:468px;">Bearnaise.<span class="price">2,95 €</span><span class="sep">·</span>de Champiñones.<span class="price">2,65 €</span></p>

  <h2 class="heading" style="left:903px; top:528px;">Los Postres de la Volière</h2>
  <ul class="menu-list menu-list--right" style="top:560px;">
    <li class="item item--compact"><span>Frambuesas “La Volière”</span><span class="price">6,25 €</span></li>
    <li class="item item--compact"><span>Cocktail de Frutas Exóticas</span><span class="price">5,25 €</span></li>
    <li class="item item--compact"><span>Sorbete de Limón, Coulis de Fresa y Vodka</span><span class="price">5,50 €</span></li>
    <li class="item item--compact"><span>Pastel de Chocolate Casero con su Salsa de Vainilla</span><span class="price">6,25 €</span></li>
    <li class="item item--compact"><span>Crême Brulée</span><span class="price">6,25 €</span></li>
    <li class="item item--compact"><span>Tarta de Manzana Casera “Tatín” y su Helado de Vainilla</span><span class="price">6,95 €</span></li>
    <li class="item item--compact"><span>Copa Glacier Nord</span><span class="price">6,75 €</span></li>
    <li class="item item--compact"><span>Pera al Chocolate Caliente y Helado de Macadamia</span><span class="price">5,95 €</span></li>
    <li class="item item--compact"><span>Tarta de Queso con Coulis de Fresa</span><span class="price">5,75 €</span></li>
    <li class="item item--compact"><span>Nuestra Mousse de Chocolate</span><span class="price">5,75 €</span></li>
  </ul>

</main>
</body>
</html>
```